Birch & Ember Website Design (Rustic/Western)

OVERVIEW
Birch & Ember Supply House (aka Birch & Ember) manufactures rustic / western furniture and décor for cabins, lodges, and ranches. We also offer a line of accessories to complement our product line.
WEB PAGE (www.BirchAndEmber.example)
We are looking for a new web page design to represent our mountain-style (log furniture) and country-style (barnwood furniture) product line. We would like to re-create our existing homepage with a similar style template for our product line.
Our website is currently under construction – a draft has been published as an example outline. We are currently using Plinkora.example for our online store.
THEME
The overall theme needs to appear rustic, yet elegant. Listed below are only suggestions, not requirements. Please use your own creativity.
* Photographs: We will use our own photographs, for now any photograph will suffice.
* Background Colors: dark brown (rgb 21-9-2), medium brown (rgb 39-17-4), light brown (rgb 72-34-3). White background is also an option.
* Font Colors: beige (rgb 233-164-118), gold (rgb 151-98-2)
• Mountain-Style Images: cabin, wildlife, mountains, fishing, wildlife, trees, etc.
* Mountain-Style Colors: hunter green
* Country-Style Images: western, ranch, barn, farm animals, horse buggies, horseshoes, etc.
* Country-Style Colors: maroon
Thanks to all who are participating.
Target Market(s)
Outdoor enthusiasts who enjoy mountain living or country living. Our primary target market is our local market and within a 100 mile radius of our location.
Industry/Entity Type
Construction
Requirements
Must have
- Rustic, yet elegant design.
Homepage and product template page for displaying each item.
Nice to have
- Source code and functionality is optional.
Mountain-Style theme to represent our collection of log furniture and décor suited for cabins and lodges. Suggested color: hunter green. Images may include cabin, wildlife, mountains, fishing, wildlife, trees, etc.
Country-Style theme to represent our collection of barnwood furniture and décor suited for farms and ranches. Suggested color: maroon. Images may include western, ranch, barn, farm animals, horse buggies, horseshoes, etc.

```html
<!DOCTYPE html>
<html lang="en">
<head>
<meta charset="utf-8">
<title>Birch &amp; Ember Supply House</title>
<link rel="stylesheet" href="https://fonts.googleapis.com/css2?family=Cinzel:wght@400;700&family=Lora:ital,wght@0,400;1,400&display=swap">
<style>
:root{
  --dark:#150902;
  --medium:#271104;
  --light:#482203;
  --beige:#e9a476;
  --gold:#976202;
  --tan:#b07a4a;
  --cream:#f3d7b8;
  --panel:#6b3d1c;
}
*{box-sizing:border-box;margin:0;padding:0}
html,body{width:726px;height:1200px;overflow:hidden}
body{
  position:relative;
  background:radial-gradient(ellipse at 50% 30%,var(--light) 0%,var(--medium) 45%,var(--dark) 100%);
  font-family:"Lora",Georgia,serif;
  color:var(--beige);
}
.heading-font{font-family:"Cinzel",Georgia,serif}

/* header */
.site-header{position:absolute;top:0;left:0;width:726px;height:88px}
.social{position:absolute;left:86px;top:34px;display:flex;gap:6px}
.social span{width:18px;height:18px;border-radius:50%;border:1.5px solid var(--beige);display:block}
.brand{position:absolute;left:263px;top:10px;width:200px;height:72px;text-align:center}
.brand .seal{width:34px;height:34px;border-radius:50%;background:var(--dark);border:2px solid var(--beige);margin:0 auto 4px}
.brand .name{font-family:"Cinzel",Georgia,serif;font-weight:700;font-size:16px;color:var(--cream);letter-spacing:1px}
.search{position:absolute;right:86px;top:34px;width:168px;height:20px;border:1px solid var(--beige);background:var(--dark);display:flex;align-items:center;padding:0 6px;font-size:8px;letter-spacing:1px;color:var(--beige);font-family:"Cinzel",serif}
.search svg{margin-left:auto}

/* nav */
.main-nav{position:absolute;left:80px;top:92px;width:566px;height:24px;background:linear-gradient(var(--tan),#8a5428);display:flex;justify-content:space-between;align-items:center;padding:0 14px;border-top:1px solid var(--beige);border-bottom:1px solid var(--dark)}
.main-nav a{font-family:"Cinzel",serif;font-size:8.5px;font-weight:700;color:var(--cream);text-decoration:none;letter-spacing:.5px}

/* hero */
.hero{position:absolute;left:80px;top:122px;width:566px;height:236px;border:4px solid var(--light);border-radius:0 0 50% 50% / 0 0 40px 40px;overflow:hidden}
.hero-photo{position:absolute;inset:0;background:linear-gradient(180deg,#f2b24a 0%,#d66a1c 45%,#7a2c0c 80%,#3a1405 100%)}
.hero-title{position:absolute;left:42px;top:62px;font-family:"Cinzel",serif;color:#fff;line-height:1}
.hero-title .small{font-size:26px;display:block}
.hero-title .big{font-size:50px;display:block}
.dots{position:absolute;left:50%;transform:translateX(-50%);display:flex;gap:4px}
.dots i{width:7px;height:7px;border-radius:50%;background:var(--cream);display:block;opacity:.6}
.dots i.on{opacity:1;background:#fff}

/* headings */
.section-title{position:absolute;left:0;width:726px;text-align:center;font-family:"Cinzel",serif;font-weight:700;color:var(--beige);font-size:15px;letter-spacing:1px}
.ruled{display:flex;align-items:center;justify-content:center;gap:10px}
.ruled::before,.ruled::after{content:"";height:1px;width:150px;background:var(--beige);opacity:.7}
.body-text{position:absolute;text-align:center;font-style:italic;font-size:7.6px;line-height:13px;color:var(--beige)}

/* mountain */
.mountain{position:absolute;left:60px;top:560px;width:606px;height:240px;background:var(--dark);border-top:1px solid var(--gold);border-bottom:1px solid var(--gold)}
.circles{position:absolute;left:28px;top:52px;width:550px;display:flex;justify-content:space-between}
.circle-item{width:110px;text-align:center}
.circle-photo{width:110px;height:110px;border-radius:50%;border:4px solid var(--tan)}
.circle-label{font-family:"Cinzel",serif;font-weight:700;font-size:14px;color:var(--cream);margin-top:6px}

/* country */
.country{position:absolute;left:60px;top:870px;width:606px;height:190px;background:linear-gradient(90deg,var(--panel),#8a5430);border:1px solid var(--gold)}
.country-photo{position:absolute;left:-28px;top:-10px;width:210px;height:210px;border-radius:50%;border:6px solid var(--tan);background:radial-gradient(circle at 40% 40%,#c8a27a,#8b6a45 60%,#5a3c20)}
.country-tag{position:absolute;left:218px;top:148px;font-family:"Cinzel",serif;font-weight:700;font-size:11px;color:var(--cream)}
.arrows{position:absolute;right:-8px;top:78px;display:flex;flex-direction:column;gap:6px}
.arrows span{width:16px;height:16px;border-radius:50%;background:var(--beige);display:flex;align-items:center;justify-content:center}

/* quote */
.testimonial{position:absolute;left:80px;top:1078px;width:566px;height:60px;background:var(--medium);border:1px solid var(--light)}
.quote-mark{position:absolute;left:18px;top:2px;font-family:"Cinzel",serif;font-size:46px;color:var(--beige)}
.testimonial p{position:absolute;left:66px;top:16px;width:330px;font-style:italic;font-size:7.6px;line-height:13px;color:var(--beige)}
.read-more{position:absolute;right:30px;top:20px;width:80px;height:20px;background:var(--beige);color:var(--dark);font-size:8px;display:flex;align-items:center;justify-content:center}

.site-footer{position:absolute;left:80px;top:1172px;font-size:7px;color:var(--beige)}
</style>
</head>
<body>

<header class="site-header">
  <div class="social"><span></span><span></span><span></span><span></span><span></span></div>
  <div class="brand"><div class="seal"></div><div class="name">Birch &amp; Ember</div></div>
  <div class="search">SEARCH
    <svg width="9" height="9" viewBox="0 0 10 10"><circle cx="4" cy="4" r="3" fill="none" stroke="#e9a476" stroke-width="1.4"/><line x1="6.2" y1="6.2" x2="9" y2="9" stroke="#e9a476" stroke-width="1.4"/></svg>
  </div>
</header>

<nav class="main-nav">
  <a href="#">HOME</a><a href="#">FURNITURE</a><a href="#">LAMPS</a><a href="#">WALL DÉCOR</a><a href="#">ACCESSORIES</a><a href="#">BARGAINS</a><a href="#">CONTACT</a>
</nav>

<section class="hero">
  <div class="hero-photo" role="img" aria-label="Photo of red rock mountain ridges at sunset"></div>
  <div class="hero-title"><span class="small">BIRCH&amp;</span><span class="big">EMBER</span></div>
  <div class="dots" style="bottom:16px"><i class="on"></i><i></i><i></i></div>
</section>

<h2 class="section-title" style="top:432px">WELCOME TO BIRCH &amp; EMBER</h2>
<p class="body-text" style="left:150px;top:462px;width:426px">Birch &amp; Ember began as a small family workshop building sturdy furniture for cabins, lodges and ranches. Each piece is cut, sanded and finished by hand from native logs and reclaimed barnwood. Over the years we added lamps, wall décor and accessories to round out the rustic home, and we still deliver most orders ourselves.</p>

<section class="mountain">
  <h2 class="section-title ruled" style="top:16px;width:606px">MOUNTAIN-STYLE COLLECTION</h2>
  <div class="circles">
    <div class="circle-item"><div class="circle-photo" role="img" aria-label="Photo of a log cabin in the woods" style="background:radial-gradient(circle,#9a6a3a,#4a2a12)"></div><div class="circle-label">CABIN</div></div>
    <div class="circle-item"><div class="circle-photo" role="img" aria-label="Photo of wildlife in a green meadow" style="background:radial-gradient(circle,#8a8a4a,#3e4a1e)"></div><div class="circle-label">WILDLIFE</div></div>
    <div class="circle-item"><div class="circle-photo" role="img" aria-label="Photo of mountains under a blue sky" style="background:linear-gradient(#8fb4d8,#6a7f5a 60%,#3d4a2a)"></div><div class="circle-label">MOUNTAINS</div></div>
    <div class="circle-item"><div class="circle-photo" role="img" aria-label="Photo of people fishing by a lake" style="background:linear-gradient(#bcd2e0,#7a9a7a 55%,#4a5a3a)"></div><div class="circle-label">FISHING</div></div>
  </div>
  <p class="body-text" style="left:90px;top:194px;width:426px">Our log collection is built from hand-peeled pine and cedar, made to feel at home in a mountain cabin or a lakeside lodge. Browse beds, tables, benches and lamps crafted for lasting comfort.</p>
  <div class="dots" style="bottom:8px"><i class="on"></i><i></i><i></i><i></i></div>
</section>

<h2 class="section-title ruled" style="top:838px">COUNTRY-STYLE COLLECTION</h2>
<section class="country">
  <div class="country-photo" role="img" aria-label="Photo of zebras and giraffes on a dry plain"></div>
  <p class="body-text" style="left:218px;top:22px;width:350px;text-align:left">Our barnwood line brings the warmth of the old ranch indoors. Weathered boards, iron hardware and honest joinery come together in tables, cabinets, benches and shelves that wear their history proudly. Each piece is made to order in our shop and finished with a natural oil that deepens with age.</p>
  <div class="country-tag">RUSTIC / WESTERN FURNITURE &amp; ACCESSORIES</div>
  <div class="arrows">
    <span><svg width="8" height="8" viewBox="0 0 8 8"><path d="M2 1l3 3-3 3" fill="none" stroke="#150902" stroke-width="1.5"/></svg></span>
    <span><svg width="8" height="8" viewBox="0 0 8 8"><path d="M6 1L3 4l3 3" fill="none" stroke="#150902" stroke-width="1.5"/></svg></span>
  </div>
</section>

<section class="testimonial">
  <div class="quote-mark">“</div>
  <p>Birch &amp; Ember built our dining table from the old barn on our land. It is the heart of our home now.</p>
  <div class="read-more">Continue Reading</div>
</section>

<footer class="site-footer">© 2014 Birch &amp; Ember. All Rights Reserved</footer>

</body>
</html>
```